Business Card for a new businees.

need a very good business for a new company based in Riverside California call Levy Lantern LLC. We help client file taxes, resolve tax debt and attain peace of mind We help people nationwide solve Tax problems. We help with Installment agreements, Offers in Compromise, Partial Pay Installment Agreements, Currently Not Collectible status, Liens and Levy Removal, Garnishment removal. We offer individualized services

Target Market(s)

Any one with Tax Problems nationwide. My clients span across age, occupation etc

Contact Information for Business Card

Card must be attractive and have enough information to let client know we care and call us

Colors

Designer to choose colors to be used in the design.

Requirements
Must have
• the basics and then surprise me
Nice to have
• surprise m

```html
<!DOCTYPE html>
<html lang="en">
<head>
<meta charset="utf-8">
<title>Levy Lantern LLC – Business Card</title>
<link rel="stylesheet" href="https://fonts.googleapis.com/css2?family=Poppins:wght@400;500;600;700&display=swap">
<style>
  :root {
    --bg-top: #8d8f93;
    --bg-bottom: #3f4145;
    --card: #141414;
    --card-edge: #1f1f1f;
    --gold: #f2c614;
    --olive: #b79a10;
    --white: #f4f4f4;
    --rule: #cfcfcf;
  }
  * { box-sizing: border-box; margin: 0; padding: 0; }
  html, body { width: 1200px; height: 1000px; overflow: hidden; }
  body {
    position: relative;
    background: linear-gradient(160deg, var(--bg-top) 0%, #6a6c70 45%, var(--bg-bottom) 100%);
    font-family: "Poppins", sans-serif;
    color: var(--white);
  }
  .card {
    position: absolute;
    width: 700px;
    height: 400px;
    border-radius: 26px;
    background: radial-gradient(ellipse at 40% 35%, var(--card-edge) 0%, var(--card) 70%);
    box-shadow: 0 18px 40px rgba(0,0,0,.45);
  }
  .card-front { left: 130px; top: 80px; }
  .card-back  { left: 370px; top: 520px; }
  .frame {
    position: absolute;
    inset: 16px;
    border: 3px solid var(--gold);
    border-radius: 16px;
  }

  /* brand lockup */
  .brand { position: absolute; }
  .brand-row { display: flex; align-items: center; gap: 12px; }
  .brand-mark { border-radius: 50%; background: var(--gold); flex: none; }
  .brand-name {
    font-weight: 700;
    color: var(--gold);
    line-height: 1;
    letter-spacing: -0.5px;
    white-space: nowrap;
  }
  .brand-bar { background: var(--gold); }
  .brand-line { font-weight: 500; white-space: nowrap; color: var(--white); }
  .brand-tag { font-weight: 500; color: var(--olive); letter-spacing: 1px; white-space: nowrap; }

  /* front */
  .card-front .brand { left: 150px; top: 78px; }
  .card-front .brand-mark { width: 30px; height: 30px; }
  .card-front .brand-name { font-size: 62px; }
  .card-front .brand-bar { width: 260px; height: 6px; margin: 12px 0 10px 42px; }
  .card-front .brand-line { font-size: 15px; letter-spacing: 4px; margin-left: 42px; }
  .card-front .brand-tag { font-size: 11px; margin: 4px 0 0 42px; }

  .services {
    position: absolute;
    left: 60px;
    right: 50px;
    top: 252px;
    list-style: none;
    display: flex;
    flex-wrap: wrap;
    gap: 8px 20px;
    font-size: 15px;
    font-weight: 500;
  }
  .services li { display: flex; align-items: center; gap: 8px; white-space: nowrap; }
  .services li::before {
    content: "";
    width: 8px; height: 8px;
    border-radius: 50%;
    background: var(--gold);
  }

  /* back */
  .card-back .brand { left: 60px; top: 62px; }
  .card-back .brand-mark { width: 20px; height: 20px; }
  .card-back .brand-name { font-size: 42px; }
  .card-back .brand-bar { width: 180px; height: 4px; margin: 8px 0 7px 32px; }
  .card-back .brand-line { font-size: 10px; letter-spacing: 3px; margin-left: 32px; }
  .card-back .brand-tag { font-size: 8px; margin: 3px 0 0 32px; }

  .holder { position: absolute; right: 52px; top: 66px; text-align: right; }
  .holder-name { color: var(--gold); font-size: 24px; font-weight: 600; letter-spacing: 3px; }
  .holder-role { font-size: 15px; letter-spacing: 5px; font-weight: 500; }
  .divider-top {
    position: absolute; left: 340px; right: 52px; top: 172px;
    height: 1px; background: var(--rule);
  }
  .address {
    position: absolute; right: 52px; top: 188px;
    text-align: right; font-size: 18px; font-weight: 500; line-height: 1.6;
    font-style: normal;
  }
  .divider-bottom {
    position: absolute; left: 44px; width: 300px; top: 265px;
    height: 1px; background: var(--rule);
  }
  .contacts {
    position: absolute; left: 50px; top: 280px;
    list-style: none; font-size: 17px; font-weight: 500;
  }
  .contacts li { display: flex; align-items: center; gap: 12px; height: 28px; }
  .contacts svg { width: 18px; height: 18px; flex: none; fill: var(--gold); }
</style>
</head>
<body>

<section class="card card-front" aria-label="Card front">
  <div class="frame"></div>
  <div class="brand">
    <div class="brand-row">
      <span class="brand-mark"></span>
      <span class="brand-name">Levy Lantern</span>
    </div>
    <div class="brand-bar"></div>
    <div class="brand-line">TAX RELIEF. TAX RETURNS.</div>
    <div class="brand-tag">YOUR TRUSTED TAX ADVOCATES. CLARITY AT EVERY STEP</div>
  </div>
  <ul class="services">
    <li>Installment agreements</li>
    <li>Offers in Compromise</li>
    <li>Garnishment removal</li>
    <li>Partial Pay Installment Agreements</li>
    <li>Currently Not Collectible status</li>
    <li>Liens and Levy Removal</li>
  </ul>
</section>

<section class="card card-back" aria-label="Card back">
  <div class="frame"></div>
  <div class="brand">
    <div class="brand-row">
      <span class="brand-mark"></span>
      <span class="brand-name">Levy Lantern</span>
    </div>
    <div class="brand-bar"></div>
    <div class="brand-line">TAX RELIEF. TAX RETURNS.</div>
    <div class="brand-tag">YOUR TRUSTED TAX ADVOCATES. CLARITY AT EVERY STEP</div>
  </div>
  <div class="holder">
    <div class="holder-name">YOUR NAME</div>
    <div class="holder-role">DIRECTOR</div>
  </div>
  <div class="divider-top"></div>
  <address class="address">4820 Orchard Ave. Ste 310<br>Riverside, CA 92501</address>
  <div class="divider-bottom"></div>
  <ul class="contacts">
    <li>
      <svg viewBox="0 0 24 24" aria-hidden="true"><path d="M6.6 10.8a15.1 15.1 0 0 0 6.6 6.6l2.2-2.2a1 1 0 0 1 1-.25 11.4 11.4 0 0 0 3.6.57 1 1 0 0 1 1 1V20a1 1 0 0 1-1 1A17 17 0 0 1 3 4a1 1 0 0 1 1-1h3.5a1 1 0 0 1 1 1c0 1.25.2 2.45.57 3.57a1 1 0 0 1-.25 1z"/></svg>
      951-555-0148
    </li>
    <li>
      <svg viewBox="0 0 24 24" aria-hidden="true"><path d="M2 5h20v14H2z M4 7v.4l8 5.3 8-5.3V7z" fill-rule="evenodd"/></svg>
      maya@levylantern.com
    </li>
    <li>
      <svg viewBox="0 0 24 24" aria-hidden="true"><path d="M12 2a10 10 0 1 0 0 20 10 10 0 0 0 0-20zm6.9 9h-3a15 15 0 0 0-1.3-5.7A8 8 0 0 1 18.9 11zM12 4.1c.9 1.2 1.8 3.6 1.9 6.9h-3.8c.1-3.300 1-5.7 1.9-6.9zM9.4 5.3A15 15 0 0 0 8.1 11h-3a8 8 0 0 1 4.3-5.7zM5.1 13h3a15 15 0 0 0 1.3 5.7A8 8 0 0 1 5.1 13zm6.9 6.9c-.9-1.2-1.8-3.6-1.9-6.9h3.8c-.1 3.3-1 5.7-1.9 6.9zm2.6-1.2a15 15 0 0 0 1.3-5.7h3a8 8 0 0 1-4.3 5.7z"/></svg>
      www.levylantern.com
    </li>
  </ul>
</section>

</body>
</html>
```